Dental Office Business Card

We need a business card for our pediatric dentistry office.
On one side the design needs to contain the following:
our logo (attached)
Vento Pediatric Grins
Soraya Kadbelani, DDS
Board Certified Pediatric Dentist
Tel: (555) 318-2747)
Fax: (555) 264-8031
Email: info@ventopediatricgrins.example
Web: www.ventopediatricgrins.example
Address: 41 Brindle Ave, Suite 208, Larkmoor, NX 02099

On the other side of the card, the design needs to have an appointment reminder (date and time as well as day of the week) similar to the design attached (no need for appointment reason “For”)

```html
<!DOCTYPE html>
<html lang="en">
<head>
<meta charset="utf-8">
<title>Vento Pediatric Grins – Business Card</title>
<link rel="stylesheet" href="https://fonts.googleapis.com/css2?family=Montserrat:wght@400;500;700;800&display=swap">
<style>
  :root {
    --ink: #231f20;
    --ink-soft: #4a4a4a;
    --mint: #a8d6a3;
    --mint-line: #8cc987;
    --rule: #b5b5b5;
    --paper: #ffffff;
    --backdrop: #2a2a2a;
  }
  * { box-sizing: border-box; margin: 0; padding: 0; }
  html, body { width: 1200px; height: 884px; overflow: hidden; }
  body {
    background: var(--backdrop);
    font-family: "Montserrat", sans-serif;
    color: var(--ink);
    position: relative;
  }
  .card {
    position: absolute;
    left: 260px;
    width: 680px;
    height: 388px;
    background: var(--paper);
    border-radius: 26px;
    overflow: hidden;
  }
  .card--front { top: 36px; }
  .card--back { top: 460px; }

  .brand {
    position: absolute;
    display: flex;
    align-items: center;
    gap: 12px;
  }
  .brand__dot {
    width: 34px; height: 34px; border-radius: 50%;
    background: var(--mint);
    flex: none;
  }
  .brand__name {
    font-weight: 800;
    font-size: 21px;
    line-height: 1.15;
    color: var(--ink);
    text-transform: uppercase;
    letter-spacing: 0.5px;
  }

  /* Front */
  .card--front .brand { right: 44px; top: 118px; }
  .holder { position: absolute; left: 44px; top: 48px; }
  .holder__name { font-weight: 800; font-size: 25px; }
  .holder__name span { font-weight: 500; }
  .holder__title { font-size: 17px; font-weight: 400; color: var(--ink-soft); margin-top: 4px; }
  .front-rule {
    position: absolute; left: 44px; top: 118px; width: 300px; height: 1.5px;
    background: var(--mint-line);
  }
  .contacts { position: absolute; left: 44px; top: 138px; list-style: none; }
  .contacts li {
    display: flex; align-items: center; gap: 10px;
    font-size: 15px; color: var(--ink-soft); margin-bottom: 6px;
  }
  .contacts svg { width: 15px; height: 15px; fill: var(--mint-line); flex: none; }
  .address-rule {
    position: absolute; left: 360px; right: 44px; top: 212px; height: 1.5px;
    background: var(--mint-line);
  }
  .address {
    position: absolute; right: 44px; top: 226px; text-align: right;
    font-size: 16px; line-height: 1.4; color: var(--ink-soft);
  }
  .band { position: absolute; left: 0; bottom: 0; width: 680px; height: 80px; }
  .website {
    position: absolute; right: 44px; bottom: 10px;
    font-size: 16px; font-weight: 500; color: var(--ink);
  }

  /* Back */
  .card--back .brand { right: 40px; top: 40px; }
  .heading { position: absolute; left: 44px; top: 36px; }
  .heading__main { font-weight: 800; font-size: 30px; }
  .heading__sub { font-size: 22px; font-weight: 400; color: var(--ink-soft); }
  .heading__rule { width: 240px; height: 1.5px; background: var(--mint-line); margin-top: 8px; }
  .field {
    position: absolute; left: 44px; right: 44px;
    display: flex; align-items: flex-end; gap: 8px;
    font-size: 15px; color: var(--ink-soft);
  }
  .field__line { flex: 1; border-bottom: 1px solid var(--rule); height: 14px; }
  .field--name { top: 150px; }
  .field--date { top: 196px; }
  .field--time { top: 318px; left: 340px; }
  .days {
    position: absolute; left: 44px; right: 44px; top: 258px;
    display: flex; justify-content: space-between; list-style: none;
    font-size: 15px; color: var(--ink-soft);
  }
  .days li { display: flex; align-items: center; gap: 8px; }
  .days li::after {
    content: ""; width: 16px; height: 16px; border: 1.5px solid var(--mint-line);
  }
</style>
</head>
<body>

<section class="card card--front" aria-label="Business card front">
  <div class="holder">
    <p class="holder__name">Soraya Kadbelani, <span>DDS</span></p>
    <p class="holder__title">Board Certified Pediatric Dentist</p>
  </div>
  <div class="front-rule"></div>
  <ul class="contacts">
    <li><svg viewBox="0 0 24 24"><path d="M6.6 10.8a15 15 0 0 0 6.6 6.6l2.2-2.2a1 1 0 0 1 1-.25 11.4 11.4 0 0 0 3.6.57 1 1 0 0 1 1 1V20a1 1 0 0 1-1 1A17 17 0 0 1 3 4a1 1 0 0 1 1-1h3.5a1 1 0 0 1 1 1c0 1.250.2 2.45.57 3.57a1 1 0 0 1-.25 1z"/></svg>(555) 318-2747)</li>
    <li><svg viewBox="0 0 24 24"><path d="M6 2h10v5H6zM4 9h16a2 2 0 0 1 2 2v7h-4v4H6v-4H2v-7a2 2 0 0 1 2-2zm4 8v3h8v-3z"/></svg>(555) 264-8031</li>
    <li><svg viewBox="0 0 24 24"><path d="M2 5h20v14H2zm2 2v.5l8 5 8-5V7z"/></svg>info@ventopediatricgrins.example</li>
  </ul>
  <div class="brand">
    <span class="brand__dot"></span>
    <p class="brand__name">Vento<br>Pediatric Grins</p>
  </div>
  <div class="address-rule"></div>
  <p class="address">41 Brindle Ave, Suite 208<br>Larkmoor, NX 02099</p>
  <svg class="band" viewBox="0 0 680 80" preserveAspectRatio="none" aria-hidden="true">
    <path d="M0 6 H290 C320 6 334 20 356 38 C330 24 316 16 290 16 H0 Z" fill="var(--ink)"/>
    <path d="M0 22 H290 C325 22 338 44 372 44 H680 V80 H0 Z" fill="var(--mint)"/>
  </svg>
  <p class="website">www.ventopediatricgrins.example</p>
</section>

<section class="card card--back" aria-label="Business card back – appointment reminder">
  <div class="heading">
    <p class="heading__main">Appointment</p>
    <p class="heading__sub">Reminder</p>
    <div class="heading__rule"></div>
  </div>
  <div class="brand">
    <span class="brand__dot"></span>
    <p class="brand__name">Vento<br>Pediatric Grins</p>
  </div>
  <div class="field field--name"><span>Name:</span><span class="field__line"></span></div>
  <div class="field field--date"><span>Date :</span><span class="field__line"></span></div>
  <ul class="days">
    <li>Mon.</li><li>Tue.</li><li>Wed.</li><li>Thu.</li><li>Fri.</li><li>Sat.</li>
  </ul>
  <div class="field field--time"><span>Time:</span><span class="field__line"></span><span>a.m / p.m</span></div>
</section>

</body>
</html>
```